Harborline Cremations Business Cards

To create a business card for my company Harborline Cremations. Remember it is a cremation company.
We want to make sure people have a business card and information. Something modern, professional
100% Online
Prices starting at $695 all-inclusive (prices subject to change without notice).
A business card is the first point of contact with the prospective client.

Contact Information for Business Card

(305) 418-7260
www.HarborlineCremationsMiami.example
harborlinecremations@mailbox.example

Requirements
Must have
• 100% Online
Prices starting at $695 all-inclusive (prices subject to change without notice)

(305) 418-7260

Must match logo style
Should not have
• No black backgrounds. Please only use the white, orange and blue from the logo

```html
<!DOCTYPE html>
<html lang="en">
<head>
<meta charset="utf-8">
<title>Harborline Cremations – Business Card</title>
<link rel="stylesheet" href="https://fonts.googleapis.com/css2?family=Montserrat:wght@400;500;600;700;800&display=swap">
<style>
  :root {
    --brand-blue: #1f6fc0;
    --brand-blue-deep: #1a5fa8;
    --brand-orange: #ee7a2c;
    --card-white: #ffffff;
    --backdrop: #e9eef3;
    --fine-grey: #4a6a8c;
  }
  * { margin: 0; padding: 0; box-sizing: border-box; }
  html, body {
    width: 1200px; height: 900px; overflow: hidden;
    background: var(--backdrop);
    font-family: "Montserrat", sans-serif;
  }
  .business-card {
    position: absolute; left: 80px; top: 154px;
    width: 1040px; height: 592px;
    background: var(--card-white);
    border-radius: 6px;
    box-shadow: 0 10px 30px rgba(30, 60, 90, 0.15);
  }
  .brand {
    position: absolute; left: 40px; top: 50px; width: 400px;
    display: flex; flex-direction: column; align-items: center;
  }
  .brand-sun {
    width: 180px; height: 180px; border-radius: 50%;
    background: var(--brand-orange);
    margin-bottom: 24px;
  }
  .brand-name {
    color: var(--brand-blue);
    font-weight: 600;
    text-align: center;
    line-height: 1.1;
    text-transform: uppercase;
  }
  .brand-name .line-main { display: block; font-size: 52px; letter-spacing: 3px; }
  .brand-name .line-sub { display: block; font-size: 24px; letter-spacing: 7px; margin-top: 4px; }
  .contact-list {
    position: absolute; left: 48px; top: 438px;
    list-style: none;
    color: var(--brand-blue);
    font-size: 24px; font-weight: 500;
  }
  .contact-list li { display: flex; align-items: center; gap: 12px; height: 37px; }
  .contact-list svg { width: 24px; height: 24px; flex: none; fill: var(--brand-blue); }
  .price-badge { position: absolute; left: 0; top: 0; width: 1040px; height: 592px; }
  .badge-arc { font-weight: 600; font-size: 34px; letter-spacing: 2px; fill: var(--brand-blue); }
  .badge-online { font-weight: 700; font-size: 28px; fill: var(--brand-blue-deep); }
  .badge-price { font-weight: 800; font-size: 100px; fill: var(--brand-blue-deep); }
  .badge-note { font-weight: 400; font-size: 11px; fill: var(--fine-grey); }
</style>
</head>
<body>
<main class="business-card">
  <div class="brand">
    <div class="brand-sun"></div>
    <h1 class="brand-name">
      <span class="line-main">Harborline</span>
      <span class="line-sub">Cremations</span>
    </h1>
  </div>

  <ul class="contact-list">
    <li>
      <svg viewBox="0 0 24 24" aria-hidden="true"><path d="M6.6 10.8a15.1 15.1 0 0 0 6.6 6.6l2.2-2.2c.3-.3.7-.4 1-.2 1.1.4 2.3.6 3.6.6.6 0 1 .4 1 1V20c0 .6-.4 1-1 1A17 17 0 0 1 3 4c0-.6.4-1 1-1h3.5c.6 0 1 .4 1 1 0 1.3.2 2.5.6 3.6.1.3 0 .7-.2 1z"/></svg>
      (305) 418-7260
    </li>
    <li>
      <svg viewBox="0 0 24 24" aria-hidden="true"><path d="M2 5h20v14H2zM4 7v.5l8 5 8-5V7l-8 5z"/></svg>
      harborlinecremations@mailbox.example
    </li>
    <li>
      <svg viewBox="0 0 24 24" aria-hidden="true"><path d="M12 2a10 10 0 1 0 0 20 10 10 0 0 0 0-20zm0 2c.9 0 2.2 2 2.7 5H9.3C9.8 6 11.1 4 12 4zM9.1 11h5.8a17 17 0 0 1 0 2H9.1a17 17 0 0 1 0-2zm-2 0a19 19 0 0 0 0 2H4.2a8 8 0 0 1 0-2zm9.8 0h2.9a8 8 0 0 1 0 2h-2.9a19 19 0 0 0 0-2zM9.3 15h5.4c-.5 3-1.8 5-2.7 5s-2.2-2-2.7-5z"/></svg>
      www.HarborlineCremationsMiami.example
    </li>
  </ul>

  <svg class="price-badge" viewBox="0 0 1040 592" aria-label="Prices starting at $695, 100% online, all-inclusive">
    <defs>
      <path id="arc-top" d="M 632 305 A 168 168 0 0 1 968 305"/>
      <path id="arc-bottom" d="M 606 290 A 194 194 0 0 0 994 290"/>
    </defs>
    <text class="badge-arc"><textPath href="#arc-top" startOffset="50%" text-anchor="middle">PRICES STARTING AT</textPath></text>
    <text class="badge-online" x="800" y="236" text-anchor="middle">100% Online</text>
    <text class="badge-price" x="800" y="346" text-anchor="middle">$695</text>
    <text class="badge-note" x="800" y="390" text-anchor="middle">*prices subject to change without notice</text>
    <text class="badge-arc"><textPath href="#arc-bottom" startOffset="50%" text-anchor="middle">ALL-INCLUSIVE</textPath></text>
  </svg>
</main>
</body>
</html>
```